OpenLeaf app needs an improved design

OpenLeaf makes available books that have been banned in certain countries. The current version of the app is available for download here: https://apps.vendrix-market.example/details?id=org.brightmoss.openleaf

At the moment, the app is available only in Chinese. Books are made available within the app, in text or audio format. Books can be downloaded for offline use. We created the app as a way to circumvent the intense censorship that is placed on book distribution inside China. The app is designed in such a way that the authorities are not able to censor the app, thus users in China are able to download the app, read content and receive updates to the app. So far over 100,000 people have used the app. Books are made available to the users for free and the app is also free to download.

We have used a similar anti-censorship strategy in a number of other apps, all with equally successful outcomes.

The app is only available on Android. While many Chinese purchase high end Android devices, Android is also the operating system of choice for new internet users in China. Oftentimes, the first time a user accesses the internet will be through an inexpensive Android smartphone.

This is very much a content driven app, with limited functionality but very visual. We need to optimize the app so that it is suitable for reading long texts. While we make available banned books through the app itself, our users are primarily avid readers - they are not likely to be netizens who wanted to download a book app just because it contains banned books. They will be readers who are interested in reading and exploring new books that are not normally available to them.

The app should have similar functionality to an e-reader, like a Pagette, however it needs to be optimized for smaller screens. Apps like Scrollnest present content in an easy to read format.

Target Market(s)

Our current end users are Chinese who are professionals and have an interest in reading. They are likely between the ages of 18-50. We try to make the app as easy and intuitive as possible. Even though there are over 700 million people online in China, another 600 million of them will come online soon. We want experienced internet and technology users to easily find the content they are looking for and we want new internet and technology users to be able to easily use the app. Our users mainly use the app in the comfort of their own home - as they would read an e-book (Pagette) or in a quiet cafe.

Industry/Entity Type

Book Publisher

Font styles to use
Serif

Colors

Designer to choose colors to be used in the design.

Requirements
Must have
• Our current challenges include:
• - We want to promote new books as well as popular books (and potentially other categories) and allow users to browse more books in that category.
• - Allow users to search.
• - For each book, we need an indication whether it is an audio book or a text book.
• - For each book, we need an indication whether the book has already been downloaded.
• Our current audio book challenges include:
• - Show book cover.
• - Include all standard audio playback functions (pause, play, next chapter etc).
• - Audio books can play in the background. When the user leaves this view, the app needs to indicate that an audio book is playing in the background, and show the user how to return to this interface (to pause playback, etc).
• Our current text book challenges include:
• - Show name of book.
• - Maximize use of screen (since it may be hard to read on a small device).
• - Allow user to easily navigate (next page, any page number etc).

```html
<!DOCTYPE html>
<html lang="zh-Hant">
<head>
<meta charset="utf-8">
<title>OpenLeaf 閱讀器</title>
<link rel="stylesheet" href="https://fonts.googleapis.com/css2?family=Noto+Serif+TC:wght@400;500&family=Noto+Sans+TC:wght@400;500&display=swap">
<style>
  :root {
    --backdrop: #e7e5e1;
    --screen: #ffffff;
    --bar: #eeeeee;
    --nav: #d9d9d9;
    --ink: #1c1c1c;
    --muted: #9a9a9a;
    --icon: #3a3a3a;
    --accent: #6ec3cf;
    --track: #3c3c3c;
  }
  * { box-sizing: border-box; margin: 0; padding: 0; }
  html, body { width: 1200px; height: 1000px; overflow: hidden; }
  body {
    background: var(--backdrop);
    display: flex; align-items: center; justify-content: center;
  }
  .reader-screen {
    width: 470px; height: 836px;
    background: var(--screen);
    display: flex; flex-direction: column;
    overflow: hidden;
    box-shadow: 0 6px 30px rgba(0,0,0,.12);
  }
  .status-bar {
    height: 26px; background: var(--bar);
    display: flex; justify-content: flex-end; align-items: center; gap: 6px;
    padding: 0 12px;
    font: 500 13px "Noto Sans TC", sans-serif; color: #555;
  }
  .app-bar {
    height: 58px; background: var(--bar);
    display: flex; align-items: center; padding: 0 14px; gap: 12px;
  }
  .chapter-mark { width: 18px; height: 18px; background: var(--accent); opacity: .7; }
  .chapter-title {
    flex: 1; font: 400 21px "Noto Serif TC", serif; color: var(--muted); letter-spacing: 2px;
  }
  .toolbar { display: flex; gap: 20px; align-items: center; }
  .toolbar svg { display: block; }
  .page-text {
    flex: 1; overflow: hidden;
    padding: 10px 18px 0;
    font: 400 21.5px/1.36 "Noto Serif TC", serif; color: var(--ink);
    text-align: justify;
  }
  .page-text p { text-indent: 2em; }
  .reading-controls {
    height: 62px; background: var(--screen);
    display: flex; align-items: center; gap: 18px; padding: 0 16px;
    border-top: 1px solid #e4e4e4;
  }
  .page-slider { flex: 1; position: relative; height: 24px; }
  .page-slider .track { position: absolute; left: 0; right: 0; top: 11px; height: 2px; background: var(--track); }
  .page-slider .progress { position: absolute; left: 0; width: 30px; top: 11px; height: 2px; background: var(--accent); }
  .page-slider .knob {
    position: absolute; left: 22px; top: 0; width: 24px; height: 24px; border-radius: 50%;
    background: #fff; border: 4px solid var(--accent);
  }
  .page-slider .knob::after {
    content: ""; position: absolute; inset: 4px; border-radius: 50%; background: var(--accent); opacity: .6;
  }
  .page-count { font: 400 18px "Noto Sans TC", sans-serif; color: var(--muted); }
  .page-count strong { color: var(--ink); font-weight: 500; }
  .system-nav {
    height: 54px; background: var(--nav);
    display: flex; justify-content: space-around; align-items: center;
  }
</style>
</head>
<body>
  <main class="reader-screen">
    <div class="status-bar">
      <svg width="52" height="14" viewBox="0 0 52 14" aria-hidden="true">
        <rect x="2" y="9" width="3" height="5" fill="#666"/><rect x="7" y="6" width="3" height="8" fill="#666"/>
        <rect x="12" y="3" width="3" height="11" fill="#666"/><rect x="17" y="0" width="3" height="14" fill="#666"/>
        <rect x="30" y="1" width="8" height="13" rx="1" fill="#666"/><rect x="32" y="0" width="4" height="2" fill="#666"/>
      </svg>
      <span>12:45</span>
    </div>
    <header class="app-bar">
      <span class="chapter-mark"></span>
      <h1 class="chapter-title">作者前言</h1>
      <div class="toolbar">
        <svg width="30" height="26" viewBox="0 0 30 26" aria-label="字體大小">
          <path d="M2 3h16M10 3v20M17 11h11M22.5 11v12" stroke="var(--icon)" stroke-width="2.6" fill="none"/>
        </svg>
        <svg width="28" height="28" viewBox="0 0 28 28" aria-label="亮度">
          <circle cx="14" cy="14" r="5.5" stroke="var(--icon)" stroke-width="2.2" fill="none"/>
          <g stroke="var(--icon)" stroke-width="2.2">
            <path d="M14 1v4M14 23v4M1 14h4M23 14h4M4.8 4.8l2.8 2.8M20.4 20.4l2.8 2.8M4.8 23.2l2.8-2.8M20.4 7.6l2.8-2.8"/>
          </g>
        </svg>
        <svg width="28" height="28" viewBox="0 0 28 28" aria-label="搜尋">
          <circle cx="12" cy="12" r="9" stroke="var(--icon)" stroke-width="2.4" fill="none"/>
          <path d="M18.5 18.5L26 26" stroke="var(--icon)" stroke-width="2.6"/>
        </svg>
      </div>
    </header>
    <article class="page-text">
      <p>六四血腥鎮壓事件已經過去廿八年了。但由於種種原因，許多事實真相至今仍然不明不白，或爭議不斷。對於一場曾經震驚世界和改變了世界格局的重大歷史事件而言，這是很不應該的，也是令人頗為痛心的事情。</p>
      <p>捷克流亡作家韋林·索德拉曾經說過：「人與強權的鬥爭，即記憶與遺忘的鬥爭。」在一九六八年捷克「布拉格之春」血腥鎮壓事件之後，捷克統治者所做的全部工作，就是要人民忘記這件事；而捷克獨立知識份子所做的全部工作，就是要人民不要忘記這件事。</p>
      <p>六四血腥鎮壓事件之後的情形也是這樣。中共當局一再開動各種宣傳機器，極力掩蓋與回避六四血腥鎮壓的事實真相。而海內外的許多有識之士，卻一直致力於「毋忘六四」的工作，儘管也有些人在配合殺人者，呼籲人們忘記這件事，忘記這一天。</p>
      <p>本人作為六四血腥鎮壓事件的親身經歷者之一，尤其是作為一名在城東大學接受過專業訓練的中國古典文獻學者，感覺有義務和責任為該事件留下一份可靠而完整的歷史記錄。為此，在一九九零年的一個寒冷的深夜，本人冒設</p>
    </article>
    <div class="reading-controls">
      <svg width="22" height="28" viewBox="0 0 22 28" aria-label="書籤">
        <path d="M3 2h16v23l-8-6-8 6z" stroke="var(--icon)" stroke-width="2.2" fill="none" stroke-linejoin="round"/>
      </svg>
      <div class="page-slider" aria-label="頁面進度">
        <span class="track"></span><span class="progress"></span><span class="knob"></span>
      </div>
      <span class="page-count"><strong>9</strong>/356</span>
    </div>
    <nav class="system-nav">
      <svg width="20" height="20" viewBox="0 0 20 20" aria-label="返回"><path d="M16 2v16L3 10z" stroke="#555" stroke-width="1.8" fill="none" stroke-linejoin="round"/></svg>
      <svg width="20" height="20" viewBox="0 0 20 20" aria-label="主畫面"><circle cx="10" cy="10" r="8" stroke="#555" stroke-width="1.8" fill="none"/></svg>
      <svg width="20" height="20" viewBox="0 0 20 20" aria-label="最近應用"><rect x="2" y="2" width="16" height="16" stroke="#555" stroke-width="1.8" fill="none"/></svg>
    </nav>
  </main>
</body>
</html>
```